Looking for a cool & simple business-card-design for digital agency

Hi!

We are a web agency that offers Reputation Management, Vextra & Seo Services and software development. We like cool things, we like innovative styles.

We have uploaded our logo.

Project Deadline Extended Reason: Client does not want any designs with the colorful logo. Please send us submissions ONLY with the blac and white logo. What the client would like to see:1) Back of the card: is a silver logo on a black background2) front of the card with all the data, please use white background and black logo thank you Added Friday, May 8, 2015

```html
<!DOCTYPE html>
<html lang="en">
<head>
<meta charset="utf-8">
<title>Lumora AG – Business Card</title>
<link rel="stylesheet" href="https://fonts.googleapis.com/css2?family=Open+Sans:ital,wght@0,400;0,600;0,700;1,700&display=swap">
<style>
  :root {
    --stage: #333333;
    --card: #ffffff;
    --ink: #231f20;
    --muted: #8a8a8a;
    --rule: #bdbdbd;
    --band: #231f20;
    --back: #1a1819;
    --silver: #c6c6c6;
  }
  * { margin: 0; padding: 0; box-sizing: border-box; }
  html, body { width: 1200px; height: 907px; overflow: hidden; }
  body {
    background: var(--stage);
    font-family: "Open Sans", Arial, sans-serif;
    color: var(--ink);
    position: relative;
  }
  .card {
    position: absolute;
    left: 300px;
    width: 600px;
    background: var(--card);
    box-shadow: 0 4px 10px rgba(0,0,0,0.5);
  }
  .card--front { top: 91px; height: 341px; }
  .card--back { top: 472px; height: 343px; background: var(--back); }

  .brand {
    position: absolute;
    left: 0; right: 0;
    display: flex;
    align-items: center;
    justify-content: center;
    gap: 18px;
  }
  .card--front .brand { top: 70px; }
  .brand__mark { width: 34px; height: 34px; background: var(--ink); }
  .brand__text { display: flex; flex-direction: column; }
  .brand__name {
    font-weight: 700; font-size: 40px; line-height: 1; letter-spacing: 5px; white-space: nowrap;
  }
  .brand__tagline {
    font-weight: 400; font-size: 15px; letter-spacing: 8px; margin-top: 6px; white-space: nowrap;
  }

  .person {
    position: absolute; right: 342px; top: 180px; text-align: right;
  }
  .person__name { font-size: 20px; font-weight: 600; line-height: 26px; }
  .person__title { font-size: 16px; font-weight: 600; color: var(--muted); line-height: 24px; }
  .person__address { font-size: 14px; line-height: 20px; margin-top: 3px; }

  .divider {
    position: absolute; left: 283px; top: 184px; width: 1px; height: 87px; background: var(--rule);
  }

  .contacts { position: absolute; left: 306px; top: 182px; list-style: none; }
  .contacts li {
    display: flex; align-items: center; gap: 8px;
    font-size: 14px; line-height: 22.5px;
  }
  .contacts svg { width: 15px; height: 15px; fill: var(--ink); }

  .front-rule {
    position: absolute; left: 0; right: 0; top: 314px; height: 2px; background: var(--rule);
  }
  .front-band {
    position: absolute; left: 0; right: 0; top: 318px; bottom: 0; background: var(--band);
  }

  .card--back .brand { top: 118px; }
  .card--back .brand__name { font-size: 56px; letter-spacing: 4px; color: var(--silver); }
  .back-web {
    position: absolute; left: 0; right: 0; top: 282px;
    text-align: center; font-size: 13px; font-weight: 700; font-style: italic; letter-spacing: 4px;
    color: var(--silver);
  }
</style>
</head>
<body>
  <section class="card card--front">
    <div class="brand">
      <span class="brand__mark"></span>
      <div class="brand__text">
        <span class="brand__name">Lumora AG</span>
        <span class="brand__tagline">DIGITALE STRATEGIEN</span>
      </div>
    </div>

    <div class="person">
      <p class="person__name">Your name</p>
      <p class="person__title">Job Title</p>
      <p class="person__address">Suite 102 Street name<br>State, Zip 2034,Country</p>
    </div>

    <div class="divider"></div>

    <ul class="contacts">
      <li><svg viewBox="0 0 16 16"><path d="M3 1l3 3-2 2c1 2 3 4 5 5l2-2 3 3-2 3C6 15 1 9 1 3z"/></svg>127 345 9876</li>
      <li><svg viewBox="0 0 16 16"><path d="M4 1h8v4H4zM1 6h14v6h-2v-2H3v2H1zM4 11h8v4H4z"/></svg>345 345 9876</li>
      <li><svg viewBox="0 0 16 16"><path d="M1 3h14v1L8 9 1 4zM1 6l7 5 7-5v7H1z"/></svg>info@yourname.com</li>
      <li><svg viewBox="0 0 16 16" fill="none"><g stroke="#231f20" stroke-width="1.2" fill="none"><circle cx="8" cy="8" r="6.5"/><ellipse cx="8" cy="8" rx="3" ry="6.5"/><path d="M1.5 8h13M2.5 4.5h11M2.5 11.5h11"/></g></svg>www.yourweb.com</li>
    </ul>

    <div class="front-rule"></div>
    <div class="front-band"></div>
  </section>

  <section class="card card--back">
    <div class="brand">
      <span class="brand__name">Lumora AG</span>
    </div>
    <p class="back-web">www.yourweb.com</p>
  </section>
</body>
</html>
```